Need a Hollin & Co
* logo
* word and powerpoint livery
* basic webpage

Hollin & Co is a Private M&A Advisor. We want to look like http://www.vantrelcapital.example
It needs to communicate reliabity, conservativeness and discretion.

```html
<!DOCTYPE html>
<html lang="en">
<head>
<meta charset="utf-8">
<title>Hollin &amp; Co — Private M&amp;A Advisor</title>
<link rel="stylesheet" href="https://fonts.googleapis.com/css2?family=Carlito:wght@400;700&display=swap">
<style>
:root{
  --brand:#2a6fc4;
  --ink:#222;
  --text:#333;
  --muted:#666;
  --link:#1f6aa8;
  --band:#ededed;
  --rule:#dcdcdc;
  --page:#fff;
}
*{box-sizing:border-box;margin:0;padding:0}
html,body{width:1200px;height:1194px;overflow:hidden;background:var(--page)}
body{font-family:"Carlito",sans-serif;color:var(--text);font-size:14px;position:relative}
.site{position:absolute;left:59px;width:1097px;top:0;height:1194px}
.brand{position:absolute;top:33px;left:0}
.brand-name{font-weight:700;font-size:31px;color:var(--brand);letter-spacing:.3px;line-height:1}
.brand-tag{font-size:14.5px;color:var(--muted);margin:6px 0 0 51px}
.search{position:absolute;right:0;top:74px;width:176px;height:26px;border:1px solid #bbb;font-size:11.5px;color:#888;padding:5px 12px}
.search svg{position:absolute;right:9px;top:5px}
.main-nav{position:absolute;top:117px;left:0;width:100%;height:37px;background:var(--band);display:flex}
.main-nav a{display:block;padding:0 12px;line-height:37px;font-size:14.5px;color:var(--ink);text-decoration:none;border-right:1px solid #fff}
.main-nav a:first-child{padding-left:15px}
.main-nav a:last-child{border-right:0}
.hero{position:absolute;top:154px;left:0;width:100%;height:367px;
  background:linear-gradient(180deg,#4c74c4 0%,#7f9ed2 22%,#3c4352 52%,#4a4a44 70%,#6f8c93 86%,#9fb4b6 100%)}
.hero-arrow{position:absolute;top:173px;width:48px;height:45px;background:rgba(150,150,150,.75);display:flex;align-items:center;justify-content:center}
.hero-arrow.prev{left:28px}
.hero-arrow.next{right:25px}
.welcome{position:absolute;top:545px;left:0;width:100%;text-align:center}
.welcome h1{font-weight:400;font-size:24px;color:var(--ink)}
.welcome p{margin-top:12px;line-height:26px;font-size:14px}
.divider{position:absolute;top:722px;left:70px;width:960px;height:30px;
  background:radial-gradient(ellipse at top,rgba(0,0,0,.07),rgba(0,0,0,0) 70%);border-top:1px solid #eee}
.col{position:absolute;top:778px}
.col-about{left:0;width:530px}
.col-news{left:577px;width:520px}
.col h2{font-weight:400;font-size:24px;color:var(--ink);display:flex;align-items:center;gap:14px;height:44px}
.about-text{margin-top:12px;line-height:30.1px;font-size:14px}
.more{display:inline-block;color:var(--link);font-size:13.5px;text-decoration:none;margin-top:4px}
.news-list{list-style:none;margin-top:14px}
.news-item{position:relative;border-bottom:1px solid var(--rule);padding-bottom:10px;margin-bottom:10px}
.news-item:last-child{border-bottom:0;margin-bottom:0;padding-bottom:2px}
.news-date{font-size:13.5px;color:#555;line-height:18px}
.news-title{font-size:14px;margin-top:12px;line-height:18px}
.news-item svg{position:absolute;right:6px;bottom:10px}
.news-item:last-child svg{bottom:2px}
.footer{position:absolute;top:1106px;left:0;width:100%;height:88px;background:var(--band);text-align:center;font-size:14px;color:var(--ink)}
.footer nav{margin-top:21px}
.footer nav a{color:var(--ink);text-decoration:none;margin:0 6px}
.footer p{margin-top:12px}
</style>
</head>
<body>
<div class="site">
  <header>
    <div class="brand">
      <div class="brand-name">HOLLIN &amp; CO</div>
      <div class="brand-tag">Private M&amp;A Advisor</div>
    </div>
    <div class="search">Search
      <svg width="14" height="14" viewBox="0 0 14 14"><circle cx="6" cy="6" r="4.5" fill="none" stroke="#888" stroke-width="1.6"/><line x1="9.3" y1="9.3" x2="13" y2="13" stroke="#888" stroke-width="1.8"/></svg>
    </div>
  </header>
  <nav class="main-nav">
    <a href="#">HOME</a><a href="#">ABOUT</a><a href="#">TEAM</a><a href="#">EXPERIENCE</a><a href="#">PRESS RELEASES</a><a href="#">CAREERS</a><a href="#">CONTACT</a>
  </nav>
  <div class="hero" role="img" aria-label="Night photograph of a suspension bridge with a lit city skyline reflected in the river">
    <div class="hero-arrow prev"><svg width="12" height="18" viewBox="0 0 12 18"><polyline points="9,2 3,9 9,16" fill="none" stroke="#fff" stroke-width="1.6"/></svg></div>
    <div class="hero-arrow next"><svg width="12" height="18" viewBox="0 0 12 18"><polyline points="3,2 9,9 3,16" fill="none" stroke="#fff" stroke-width="1.6"/></svg></div>
  </div>
  <section class="welcome">
    <h1>Welcome to the Hollin &amp; Co</h1>
    <p>Lorem Ipsum is simply dummy text of the printing and typesetting industry. Lorem Ipsum has been the industry's standard dummy text ever since the 1500s, when an unknown printer took a galley of type and scrambled it to make a type specimen book. It has survived not only five centuries, but also the leap into electronic typesetting, remaining essentially unchanged. It was popularised in the 1960s with the release of Lintrex sheets containing Lorem Ipsum passages, and more recently with desktop publishing software like Alder PageSmith including versions of Lorem Ipsum.</p>
  </section>
  <div class="divider"></div>
  <section class="col col-about">
    <h2><svg width="42" height="40" viewBox="0 0 42 40"><ellipse cx="21" cy="23" rx="17" ry="12" fill="#b9b9b9"/><circle cx="21" cy="7" r="5" fill="#b9b9b9"/><rect x="9" y="30" width="6" height="8" fill="#b9b9b9"/><rect x="26" y="30" width="6" height="8" fill="#b9b9b9"/></svg>About Us</h2>
    <p class="about-text">Lorem Ipsum is simply dummy text of the printing and typesetting industry. Lorem Ipsum has been the industry's standard dummy text ever since the 1500s, when an unknown printer took a galley of type and scrambled it to make a type specimen book. It has survived not only five centuries, but also the leap into electronic typesetting, remaining essentially unchanged. It was popularised in the 1960s with the release of Lintrex sheets containing Lorem Ipsum passages, and more recently with desktop publishing software like Alder PageSmith including versions of Lorem Ipsum.</p>
    <a class="more" href="#">CLICK HERE</a>
  </section>
  <section class="col col-news">
    <h2><svg width="44" height="38" viewBox="0 0 44 38"><rect x="2" y="2" width="40" height="34" fill="none" stroke="#b9b9b9" stroke-width="3"/><rect x="8" y="9" width="28" height="4" fill="#b9b9b9"/><rect x="8" y="17" width="12" height="12" fill="#b9b9b9"/><rect x="24" y="17" width="12" height="3" fill="#b9b9b9"/><rect x="24" y="22" width="12" height="3" fill="#b9b9b9"/><rect x="24" y="27" width="12" height="3" fill="#b9b9b9"/></svg>Latest News</h2>
    <ul class="news-list">
      <li class="news-item"><div class="news-date">Jul 10 2014</div><div class="news-title">Lorem Ipsum is simply dummy text of the printing and typesetting industry.</div><svg width="10" height="18" viewBox="0 0 10 18"><polyline points="1,1 9,9 1,17" fill="none" stroke="#999" stroke-width="1.3"/></svg></li>
      <li class="news-item"><div class="news-date">Jul 03 2014</div><div class="news-title">Lorem Ipsum is simply dummy text of the printing and typesetting industry.</div><svg width="10" height="18" viewBox="0 0 10 18"><polyline points="1,1 9,9 1,17" fill="none" stroke="#999" stroke-width="1.3"/></svg></li>
      <li class="news-item"><div class="news-date">Jun 10 2014</div><div class="news-title">Lorem Ipsum is simply dummy text of the printing and typesetting industry.</div><svg width="10" height="18" viewBox="0 0 10 18"><polyline points="1,1 9,9 1,17" fill="none" stroke="#999" stroke-width="1.3"/></svg></li>
    </ul>
    <a class="more" href="#">CLICK HERE</a>
  </section>
  <footer class="footer">
    <nav><a href="#">Home</a>|<a href="#">Site Map</a>|<a href="#">Legal</a>|<a href="#">Contact</a>|<a href="#">Connect</a></nav>
    <p>Copyright © 2014 hollin&amp;coAll Rights Reserved.</p>
  </footer>
</div>
</body>
</html>
```